Casas de Nueva Aurora Flyer

Make me a flyer postcard 5 x 7 horizontal, one sided. I want main title to be "Casas de Nueva Aurora". It needs to say “Familias que se forman en la fe y valores humanos, y trabajan para llevar a otras familias al encuentro con Cristo y la Virgen María.”  We are in 4 places, include this:
Reuniones Cada Domingo
Los Olmos, Falls Church: 11:15am - 301-555-0142
Monte Claro, Sterling: 9:30am - 571-555-0187
Hogar Valle Sereno, 9:45am - 703-555-0163
Puerta Dorada, Winchester: 2:30pm - 540-555-0129
Include the logo attached, and use the picture attached as the main image, you can select the people from the image only and delete background or keep background but make it fit in nicely to the postcard.

```html
<!DOCTYPE html>
<html lang="es">
<head>
<meta charset="utf-8">
<title>Casas de Nueva Aurora</title>
<link href="https://fonts.googleapis.com/css2?family=Lato:ital,wght@0,400;0,700;0,900;1,400&family=Sacramento&display=swap" rel="stylesheet">
<style>
  :root {
    --page: #ffffff;
    --card-sky: #dceaf8;
    --brand-green: #1f6b40;
    --band-green: #247245;
    --tagline-green: #3aa864;
    --rule: rgba(255,255,255,0.35);
    --white: #ffffff;
    --gold: #a8863a;
    --gold-dark: #5e4a1c;
    --icon-red: #b1231f;
  }
  * { box-sizing: border-box; margin: 0; padding: 0; }
  html, body { width: 1200px; height: 1023px; overflow: hidden; background: var(--page); }
  .postcard {
    position: absolute; left: 0; top: 83px; width: 1200px; height: 857px; overflow: hidden;
    background: linear-gradient(180deg, var(--card-sky) 0%, #ffffff 12%, #ffffff 80%, var(--card-sky) 100%);
    font-family: "Lato", sans-serif;
  }
  .group-photo {
    position: absolute; left: 0; top: 200px; width: 1200px; height: 452px;
    background:
      linear-gradient(180deg, rgba(255,255,255,1) 0%, rgba(255,255,255,0) 22%),
      radial-gradient(ellipse at 55% 80%, #8a6e63 0%, #6f5f5a 30%, rgba(111,95,90,0) 60%),
      linear-gradient(90deg, #5d7089 0%, #4d7a47 30%, #3f6b3b 60%, #61777f 90%, #dfe8f2 100%);
  }
  .family-icon {
    position: absolute; left: 39px; top: 39px; width: 171px; height: 240px;
    background: linear-gradient(160deg, #c9a75a, var(--gold-dark));
    clip-path: polygon(0 14%, 50% 0, 100% 14%, 100% 100%, 0 100%);
    box-shadow: 0 2px 6px rgba(0,0,0,0.4);
  }
  .family-icon::after {
    content: ""; position: absolute; left: 20px; top: 40px; right: 20px; bottom: 20px;
    background: radial-gradient(circle at 50% 30%, #d9b24a 0%, var(--icon-red) 55%, #7a1814 100%);
    clip-path: polygon(0 10%, 50% 0, 100% 10%, 100% 100%, 0 100%);
  }
  .title {
    position: absolute; left: 240px; top: 70px; width: 898px; text-align: center;
    color: var(--brand-green); font-weight: 900; font-size: 61px; letter-spacing: 0.5px; line-height: 1;
    text-transform: uppercase;
  }
  .tagline {
    position: absolute; left: 260px; top: 140px; width: 850px; text-align: center;
    color: var(--tagline-green); font-style: italic; font-size: 24.5px; line-height: 35px; letter-spacing: 0.4px;
  }
  .meetings {
    position: absolute; left: 32px; top: 646px; width: 1136px; height: 181px;
    background: var(--band-green); color: var(--white);
  }
  .meetings-heading {
    position: absolute; left: 20px; top: 30px; width: 320px; text-align: center;
    font-family: "Sacramento", cursive; font-weight: 400; font-size: 58px; line-height: 52px;
  }
  .schedule { position: absolute; left: 343px; top: 22px; width: 757px; list-style: none; }
  .schedule li {
    display: grid; grid-template-columns: 1fr 16px 104px 26px 161px;
    height: 35.5px; align-items: center;
    font-weight: 700; font-size: 22px; letter-spacing: 0.2px; text-transform: uppercase;
    border-bottom: 1px solid var(--rule);
  }
  .schedule li:last-child { border-bottom: none; }
  .schedule .place { text-align: right; }
  .schedule .sep { text-align: center; }
  .schedule .phone { text-align: right; }
</style>
</head>
<body>
  <main class="postcard">
    <div class="group-photo" role="img" aria-label="Foto grupal de familias de la comunidad reunidas al aire libre entre árboles"></div>
    <div class="family-icon" role="img" aria-label="Ícono de la Sagrada Familia en marco dorado"></div>
    <h1 class="title">Casas de Nueva Aurora</h1>
    <p class="tagline">“Familias que se forman en la fe y valores humanos, y trabajan para llevar a otras familias al encuentro con Cristo y la Virgen María.”</p>
    <section class="meetings">
      <h2 class="meetings-heading">Reuniones<br>Cada Domingo</h2>
      <ul class="schedule">
        <li><span class="place">Los Olmos, Falls Church</span><span class="sep">:</span><span class="time">11:15AM</span><span class="sep">-</span><span class="phone">301-555-0142</span></li>
        <li><span class="place">Monte Claro, Sterling</span><span class="sep">:</span><span class="time">09:30AM</span><span class="sep">-</span><span class="phone">571-555-0187</span></li>
        <li><span class="place">Hogar Valle Sereno</span><span class="sep">:</span><span class="time">09:45AM</span><span class="sep">-</span><span class="phone">703-555-0163</span></li>
        <li><span class="place">Puerta Dorada, Winchester</span><span class="sep">:</span><span class="time">02:30PM</span><span class="sep">-</span><span class="phone">540-555-0129</span></li>
      </ul>
    </section>
  </main>
</body>
</html>
```